International Life/Work Balance and Personal Growth company needs a new business card

I have got the logo already and need a creative way in putting it together....

Target Market(s)

corporate - business for stress management/work/life balance seminars
anybody else who is interested in living a extraordinary life and is into Wellness and is open to changing habits

Industry/Entity Type

Business

Requirements
Must have
• must include my photo on the front

On the business card.... yes, both sides.... my name Marisol Pettark mobile 0476 581 904 www.dawnquill.com, also the facebook sign and marisol@dawnquill.com as email, also my pic see attachment and logo with slogan

Workplace Wellness Seminars
Stress Management
Law of Attraction w/s
Personal Transformations
Kestrel Yoga and Pilates

slogan: wellness ~ success ~ peace of mind
Nice to have
• I like the colors of the logo so that should match the card. I like flowing contemporary lines....something that has the feeling of peace and upliftment.

Font could be "chalkboard" or something similar....

```html
<!DOCTYPE html>
<html lang="en">
<head>
<meta charset="utf-8">
<title>Dawn Quill – Business Card</title>
<link rel="stylesheet" href="https://fonts.googleapis.com/css2?family=Ubuntu:wght@400;500;700&display=swap">
<style>
  :root {
    --page-bg: #e6e9ec;
    --navy: #1d3f8f;
    --ocean-deep: #0b557f;
    --ocean: #1677a8;
    --ocean-light: #2fa3cf;
    --leaf: #2a8a3e;
    --leaf-bright: #62b844;
    --leaf-dark: #1d6e30;
    --logo-green: #2e7a2f;
    --white: #ffffff;
    --mist: #e9efe9;
    --label-green: #3a7d2a;
  }
  html, body {
    margin: 0;
    width: 1200px;
    height: 900px;
    overflow: hidden;
    background: var(--page-bg);
    font-family: "Ubuntu", sans-serif;
  }
  .canvas {
    position: relative;
    width: 1200px;
    height: 900px;
  }
  .card {
    position: absolute;
    left: 290px;
    width: 620px;
    height: 354px;
    border-radius: 18px;
    overflow: hidden;
    box-shadow: 0 6px 18px rgba(0, 0, 0, 0.18);
  }
  .card svg.card-art {
    position: absolute;
    inset: 0;
  }
  .card-back { top: 70px; background: var(--ocean-deep); }
  .card-front { top: 476px; background: var(--white); }

  .brand {
    display: flex;
    align-items: center;
    gap: 8px;
    font-weight: 700;
    color: var(--logo-green);
    line-height: 1;
  }
  .brand-dot {
    width: 30px;
    height: 30px;
    border-radius: 50%;
    background: var(--ocean);
    flex: none;
  }

  .brand-panel {
    position: absolute;
    left: 22px;
    top: 128px;
    width: 210px;
    height: 100px;
    background: var(--white);
    display: flex;
    align-items: center;
    justify-content: center;
  }
  .brand-panel .brand { font-size: 26px; }

  .slogan {
    font-family: "Ubuntu", sans-serif;
    font-size: 15px;
    font-weight: 500;
    letter-spacing: 2px;
    word-spacing: 12px;
    fill: var(--white);
  }

  .card-front .brand {
    position: absolute;
    right: 34px;
    top: 30px;
    font-size: 22px;
  }
  .portrait {
    position: absolute;
    left: 110px;
    top: 38px;
    width: 118px;
    height: 100px;
    background: linear-gradient(180deg, #c8b3a6 0%, #d79a7a 55%, #e9763e 100%);
  }
  .person-name {
    position: absolute;
    left: 88px;
    top: 148px;
    margin: 0;
    font-size: 21px;
    font-weight: 700;
    color: var(--navy);
  }
  .contact {
    position: absolute;
    left: 300px;
    top: 60px;
    margin: 0;
    display: grid;
    grid-template-columns: 34px auto;
    row-gap: 10px;
    font-size: 14px;
  }
  .contact dt { color: var(--label-green); font-weight: 500; text-align: right; padding-right: 12px; }
  .contact dd { margin: 0; color: var(--navy); font-weight: 700; }

  .services {
    list-style: none;
    margin: 0;
    padding: 0;
  }
  .services li {
    position: absolute;
    color: var(--mist);
    font-size: 18px;
    font-weight: 700;
    line-height: 22px;
    white-space: nowrap;
  }
  .services li::before {
    content: "\2713";
    margin-right: 8px;
    color: var(--white);
  }
  .service-stress { left: 356px; top: 210px; }
  .service-transform { left: 356px; top: 244px; }
  .service-workplace { left: 34px; top: 232px; }
  .service-attraction { left: 34px; top: 266px; }
  .service-yoga { left: 196px; top: 304px; }
</style>
</head>
<body>
<main class="canvas">

  <section class="card card-back" aria-label="Card back">
    <svg class="card-art" width="620" height="354" viewBox="0 0 620 354">
      <defs>
        <linearGradient id="ocean-fill" x1="0" y1="1" x2="1" y2="0">
          <stop offset="0" stop-color="#0b557f"/>
          <stop offset="1" stop-color="#1677a8"/>
        </linearGradient>
        <linearGradient id="leaf-fill" x1="0" y1="0" x2="1" y2="1">
          <stop offset="0" stop-color="#62b844"/>
          <stop offset="1" stop-color="#2a8a3e"/>
        </linearGradient>
        <path id="slogan-path" d="M222,354 C308,250 313,145 433,55 C470,27 500,10 525,0"/>
      </defs>
      <rect width="620" height="354" fill="url(#ocean-fill)"/>
      <path class="wave-glow" d="M190,354 C282,250 292,138 412,46 C452,16 492,2 512,0 L620,0 L620,354 Z" fill="#2fa3cf" opacity="0.55"/>
      <path class="wave-white" d="M255,354 C335,250 335,150 455,60 C498,26 533,6 558,0 L620,0 L620,354 Z" fill="#ffffff"/>
      <path class="wave-green" d="M345,354 C395,295 425,235 475,150 C515,82 555,34 600,0 L620,0 L620,354 Z" fill="url(#leaf-fill)"/>
      <path class="wave-green-light" d="M420,354 C460,290 490,220 530,150 C560,96 590,50 620,20 L620,354 Z" fill="#62b844" opacity="0.7"/>
      <path class="wave-blue" d="M500,354 C530,290 560,220 620,150 L620,354 Z" fill="#2fa3cf"/>
      <text class="slogan" dominant-baseline="middle">
        <textPath href="#slogan-path" startOffset="40">WELLNESS SUCCESS PEACE OF MIND</textPath>
      </text>
    </svg>
    <div class="brand-panel">
      <div class="brand"><span class="brand-dot"></span>Dawn Quill</div>
    </div>
  </section>

  <section class="card card-front" aria-label="Card front">
    <svg class="card-art" width="620" height="354" viewBox="0 0 620 354" aria-hidden="true">
      <defs>
        <linearGradient id="field-fill" x1="0" y1="0" x2="0" y2="1">
          <stop offset="0" stop-color="#2a8a3e"/>
          <stop offset="1" stop-color="#1d6e30"/>
        </linearGradient>
      </defs>
      <path class="field" d="M0,206 C200,219 440,198 620,118 L620,354 L0,354 Z" fill="url(#field-fill)"/>
      <path class="swoosh" d="M0,190 C200,205 440,180 620,110 L620,118 C440,198 200,219 0,206 Z" fill="#1d3f8f"/>
    </svg>

    <div class="brand"><span class="brand-dot"></span>Dawn Quill</div>
    <div class="portrait" role="img" aria-label="Portrait photo of Marisol Pettark"></div>
    <h1 class="person-name">Marisol Pettark</h1>
    <dl class="contact">
      <dt>m:</dt><dd>0476 581 904</dd>
      <dt>w:</dt><dd>www.dawnquill.com</dd>
      <dt>e:</dt><dd>marisol@dawnquill.com</dd>
    </dl>

    <ul class="services">
      <li class="service-stress">Stress Management</li>
      <li class="service-transform">Personal Transformations</li>
      <li class="service-workplace">Workplace Wellness Seminars</li>
      <li class="service-attraction">Law of Attraction w/s</li>
      <li class="service-yoga">Kestrel Yoga and Pilates</li>
    </ul>
  </section>

</main>
</body>
</html>
```